Carpentry company Needs a business card design

We need a design for a Carpentry / building company, business card. Please think of designs out of the ordinary and try to make it eye catching. Our existing logo will need to be incorporated in the design. However feel free to change the colours of the logo to suit your design. I would like to see some designs with green /black and orange incorporated into it.These are not the only colours accepted and all designs that appeal will be accepted.

Please contact me should you have any questions
Thanks Marcus

Target Market(s)

General Public seeking carpentry work

Industry/Entity Type

Business

Contact Information for Business Card

- Current company logo ( colours can be changed)
-Phone number ,
- info@brantelworks.com.au
- brantelworks.com.au
-the facebook symbol

Font styles to use
Other font styles liked:
• You choose

Requirements
Must have
• Services we provide
• - Renovations
• -Deckings & Pergolas
• -Kitchens
• - Bathrooms
• - Intricate details
Nice to have
• an awesome design
Should not have
• Tools on the business card

```html
<!DOCTYPE html>
<html lang="en">
<head>
<meta charset="utf-8">
<title>Brantel Works – Business Card</title>
<link rel="stylesheet" href="https://fonts.googleapis.com/css2?family=Source+Sans+3:wght@400;600;700&display=swap">
<style>
  :root {
    --brand-red: #e1261f;
    --ink: #231f20;
    --paper: #ffffff;
    --stage: #ecebe9;
    --stripe-dark: #1e1413;
  }
  * { margin: 0; padding: 0; box-sizing: border-box; }
  html, body {
    width: 1200px; height: 900px; overflow: hidden;
    background: var(--stage);
    font-family: "Source Sans 3", "Myriad Pro", Arial, sans-serif;
  }
  .card {
    position: absolute;
    filter: drop-shadow(0 6px 14px rgba(0,0,0,0.18));
  }
  .card-shape { position: absolute; inset: 0; }
  .card--front { left: 238px; top: 60px; width: 555px; height: 345px; }
  .card--back  { left: 458px; top: 518px; width: 559px; height: 344px; }

  .wordmark {
    position: absolute;
    display: flex; align-items: center; gap: 12px;
    font-weight: 700; line-height: 1;
  }
  .wordmark__mark { width: 22px; height: 22px; flex: none; }
  .wordmark__text { display: flex; flex-direction: column; align-items: flex-end; }
  .wordmark__name { font-size: 52px; letter-spacing: 1px; }
  .wordmark__sub  { font-size: 20px; letter-spacing: 7px; margin-top: 4px; }

  .card--front .wordmark { left: 35px; top: 48px; color: var(--paper); }
  .card--front .wordmark__mark { background: var(--paper); }
  .card--back .wordmark { right: 42px; top: 44px; color: var(--ink); }
  .card--back .wordmark__mark { background: var(--brand-red); }

  .social-square {
    position: absolute; left: 472px; top: 75px;
    width: 42px; height: 42px; border-radius: 7px;
    background: var(--paper);
  }

  .holder { position: absolute; left: 35px; top: 174px; color: var(--paper); }
  .holder__name { font-size: 21px; font-weight: 600; line-height: 1.1; }
  .holder__role { font-size: 15px; font-weight: 400; margin-top: 2px; }

  .contact { position: absolute; left: 35px; top: 236px; color: var(--paper); list-style: none; }
  .contact li { font-size: 15px; line-height: 23px; }
  .contact b { font-weight: 600; }

  .services { position: absolute; right: 34px; top: 152px; text-align: right; color: var(--ink); }
  .services__title { font-size: 21px; font-weight: 700; margin-bottom: 12px; }
  .services__list { list-style: none; }
  .services__list li { font-size: 16px; line-height: 23px; }
</style>
</head>
<body>

<section class="card card--front" aria-label="Business card front">
  <svg class="card-shape" width="555" height="345" viewBox="0 0 555 345">
    <polygon points="0,0 555,0 555,180 522,205 442,210 427,280 347,345 0,345" fill="var(--brand-red)"/>
    <polyline points="347,345 427,280 442,210 522,205 555,180" fill="none" stroke="var(--stripe-dark)" stroke-width="9" stroke-linejoin="miter"/>
  </svg>
  <div class="wordmark">
    <span class="wordmark__mark"></span>
    <span class="wordmark__text">
      <span class="wordmark__name">BRANTEL</span>
      <span class="wordmark__sub">WORKS</span>
    </span>
  </div>
  <span class="social-square" aria-label="Social page"></span>
  <div class="holder">
    <p class="holder__name">Marcus Brantel</p>
    <p class="holder__role">Managing Director</p>
  </div>
  <ul class="contact">
    <li><b>T:</b> (044)-555-0192</li>
    <li><b>E:</b> info@brantelworks.com.au</li>
    <li><b>W:</b> www.brantelworks.com.au</li>
  </ul>
</section>

<section class="card card--back" aria-label="Business card back">
  <svg class="card-shape" width="559" height="344" viewBox="0 0 559 344">
    <polygon points="0,0 559,0 559,344 202,344 127,282 112,198 22,200 0,187" fill="var(--paper)"/>
    <polyline points="0,187 22,200 112,198 127,282 202,344" fill="none" stroke="var(--brand-red)" stroke-width="9" stroke-linejoin="miter"/>
  </svg>
  <div class="wordmark">
    <span class="wordmark__mark"></span>
    <span class="wordmark__text">
      <span class="wordmark__name">BRANTEL</span>
      <span class="wordmark__sub">WORKS</span>
    </span>
  </div>
  <div class="services">
    <h2 class="services__title">Services we provide</h2>
    <ul class="services__list">
      <li>Renovations</li>
      <li>Deckings &amp; Pergolas</li>
      <li>Kitchens</li>
      <li>Bathrooms</li>
      <li>Intricate details</li>
    </ul>
  </div>
</section>

</body>
</html>
```